Design fur Produktverpackung Haarschmuck
• Geforderte Formate: jpg,ai,eps., pdf
Anforderungen:
Entwerfen Sie ein Brandname für eine Haarschmuck-Linie und ein schönes Design für eine Haarschmuck-Karte (Verpackung). Um die Druckkosten in Schach zu halten, bitte nur ein- oder zweifarbig oder evtl. mit Prägedruck.
Das Design darf peppig daher kommen, soll aber wertig wirken.
Die Stanzrisse finden Sie angehängt (bitte nur auf die Stanzrisse achten, das Design und der Brandname soll neu werden).
Kartenformat: Breite 68mm, Höhe 105mm, mit Euroloch
Unternehmensbeschreibung:
Belieferer von Detailisten
Zielgruppe:
Frauen
Farben, Logo-Favoriten und weitere Anforderungen
Liebe Grüsse
Doris

```html
<!DOCTYPE html>
<html lang="de">
<head>
<meta charset="utf-8">
<title>Lunelle – Haarschmuck-Karten</title>
<link rel="stylesheet" href="https://fonts.googleapis.com/css2?family=Cormorant+Garamond:wght@500&display=swap">
<style>
  :root {
    --stage: #4d4d4d;
    --card: #ffffff;
    --ink: #8e4f48;
    --hair-light: #f3d6d1;
    --hair-mid: #e2a79e;
    --hole: #1c1c1c;
  }
  html, body {
    margin: 0;
    padding: 0;
    width: 1200px;
    height: 785px;
    overflow: hidden;
    background: var(--stage);
  }
  .stage {
    display: block;
    width: 1200px;
    height: 785px;
  }
  .card-body { fill: var(--card); }
  .brand-name {
    font-family: "Cormorant Garamond", Georgia, serif;
    font-weight: 500;
    font-size: 38px;
    letter-spacing: 1px;
    fill: var(--ink);
  }
  .pin-hole { fill: var(--hole); }
  .stop-a { stop-color: var(--hair-light); }
  .stop-b { stop-color: var(--hair-mid); }
</style>
</head>
<body>
<svg class="stage" viewBox="0 0 1200 785" xmlns="http://www.w3.org/2000/svg">
  <defs>
    <filter id="card-shadow" x="-10%" y="-10%" width="130%" height="130%">
      <feDropShadow dx="6" dy="8" stdDeviation="6" flood-color="#000" flood-opacity="0.45"/>
    </filter>
    <linearGradient id="hair-tone" x1="0" y1="0" x2="1" y2="1">
      <stop offset="0" class="stop-a"/>
      <stop offset="1" class="stop-b"/>
    </linearGradient>
    <clipPath id="spool-card-clip">
      <path d="M176,116 H480 Q496,116 496,132 V268 Q496,282 482,284 H478 Q470,284 470,296 V564 Q470,576 478,576 H482 Q496,578 496,592 V634 Q496,650 480,650 H176 Q160,650 160,634 V592 Q160,578 174,576 H178 Q186,576 186,564 V296 Q186,284 178,284 H174 Q160,282 160,268 V132 Q160,116 176,116 Z"/>
    </clipPath>
    <clipPath id="flat-card-clip">
      <rect x="644" y="116" width="348" height="534" rx="16"/>
    </clipPath>
  </defs>

  <g class="hair-card hair-card--spool">
    <path class="card-body" filter="url(#card-shadow)" fill-rule="evenodd"
      d="M176,116 H480 Q496,116 496,132 V268 Q496,282 482,284 H478 Q470,284 470,296 V564 Q470,576 478,576 H482 Q496,578 496,592 V634 Q496,650 480,650 H176 Q160,650 160,634 V592 Q160,578 174,576 H178 Q186,576 186,564 V296 Q186,284 178,284 H174 Q160,282 160,268 V132 Q160,116 176,116 Z
         M276,176 H380 Q394,176 394,191 Q394,206 380,206 H344 A16,16 0 0 1 312,206 H276 Q262,206 262,191 Q262,176 276,176 Z"/>
    <g class="hair-artwork" clip-path="url(#spool-card-clip)" role="img" aria-label="Line illustration of flowing wavy hair in rose tones">
      <path fill="url(#hair-tone)" opacity="0.75" d="M412,116 Q440,200 496,206 V116 Z"/>
      <path fill="url(#hair-tone)" opacity="0.75"
        d="M160,290 Q250,270 300,360 Q330,420 350,470 Q330,420 318,400 Q350,440 360,500 Q400,470 430,480 Q470,500 496,540 V650 H160 Z"/>
    </g>
    <text class="brand-name" x="328" y="258" text-anchor="middle">Lunelle</text>
    <circle class="pin-hole" cx="328" cy="306" r="5"/>
    <circle class="pin-hole" cx="332" cy="492" r="5"/>
  </g>

  <g class="hair-card hair-card--flat">
    <path class="card-body" filter="url(#card-shadow)" fill-rule="evenodd"
      d="M660,116 H976 Q992,116 992,132 V634 Q992,650 976,650 H660 Q644,650 644,634 V132 Q644,116 660,116 Z
         M768,176 H868 Q882,176 882,191 Q882,206 868,206 H834 A16,16 0 0 1 802,206 H768 Q754,206 754,191 Q754,176 768,176 Z"/>
    <g class="hair-artwork" clip-path="url(#flat-card-clip)" role="img" aria-label="Line illustration of flowing wavy hair in rose tones">
      <path fill="url(#hair-tone)" opacity="0.75" d="M906,116 Q930,200 992,206 V116 Z"/>
      <path fill="url(#hair-tone)" opacity="0.75"
        d="M644,290 Q740,270 790,360 Q820,420 840,470 Q820,420 806,400 Q840,440 850,500 Q890,470 920,480 Q960,500 992,540 V650 H644 Z"/>
    </g>
    <text class="brand-name" x="818" y="258" text-anchor="middle">Lunelle</text>
    <circle class="pin-hole" cx="804" cy="300" r="5"/>
    <circle class="pin-hole" cx="804" cy="392" r="5"/>
    <circle class="pin-hole" cx="804" cy="506" r="5"/>
    <circle class="pin-hole" cx="804" cy="606" r="5"/>
  </g>
</svg>
</body>
</html>
```